Business Card Design Project - bel soravin group

dear Sirs

we need business card design for our group ( BEL Soravin Group ) , i have got the Logo design of our group from pixel harbor in previous , so all need details relating to our group i think available with you, as well as the the chosen logo design

we hope to provide us with business card logo that to be appropaite and satisfactory to us .

thanks

note : logo design of our group is attached .
Updates

Reason: please extend the deadline of my project for additional 15 days because i didn't received appropriate design for our gruop yet . kindly beaware that i have received 77 design till now , supossed to send me 200-250 design at least . thanks

Target Market(s)

contents
-

name : Korvan EL Mistrani

position : Operation Manager

Industry/Entity Type

Business

Requirements
Must have

• person name

group logo
Nice to have
• logo color matching with back background

```html
<!DOCTYPE html>
<html lang="en">
<head>
<meta charset="utf-8">
<title>BEL Soravin Group – Business Card</title>
<link href="https://fonts.googleapis.com/css2?family=Open+Sans:wght@400;600&display=swap" rel="stylesheet">
<style>
  :root {
    --page-bg: #e9e6e1;
    --card-black: #050607;
    --card-black-soft: #15181c;
    --brand-blue: #2f7fd0;
    --brand-blue-deep: #1d5fa6;
    --logo-blue: #2a6fc0;
    --text-light: #f3f6fa;
    --text-muted: #b9c3cf;
  }
  * { margin: 0; padding: 0; box-sizing: border-box; }
  html, body {
    width: 1200px; height: 900px; overflow: hidden;
    background: var(--page-bg);
    font-family: "Open Sans", Arial, sans-serif;
  }
  .sheet {
    position: relative; width: 1200px; height: 900px;
    display: flex; flex-direction: column; align-items: center; justify-content: center; gap: 40px;
  }
  .card {
    position: relative; width: 700px; height: 400px; overflow: hidden;
    background: var(--card-black);
    box-shadow: 0 10px 28px rgba(0,0,0,0.28);
  }

  /* Brand name block (shared) */
  .brand-name {
    display: flex; align-items: center; gap: 14px;
    color: var(--logo-blue); font-weight: 600; text-transform: uppercase;
    line-height: 1;
  }
  .brand-name__square { width: 18px; height: 18px; background: var(--logo-blue); flex: none; }
  .brand-name__text { display: flex; flex-direction: column; gap: 6px; }

  /* Front */
  .card--front { display: flex; flex-direction: column; align-items: center; justify-content: center; }
  .card--front .brand-name__text { font-size: 58px; letter-spacing: 1px; }
  .card--front .brand-name__tagline { font-size: 27px; letter-spacing: 1px; }
  .front-web { margin-top: 30px; color: var(--text-light); font-size: 15px; letter-spacing: 2px; }

  /* Back */
  .contact-panel {
    position: absolute; top: 0; right: 0; width: 290px; height: 100%;
    background: linear-gradient(180deg, var(--brand-blue) 0%, var(--brand-blue-deep) 100%);
    padding: 78px 26px 0 34px;
  }
  .contact-list { list-style: none; display: flex; flex-direction: column; gap: 12px; }
  .contact-list li { display: flex; align-items: center; gap: 12px; color: var(--text-light); font-size: 14px; }
  .contact-list svg { width: 16px; height: 16px; flex: none; fill: var(--text-light); }

  .identity-band {
    position: absolute; left: 0; bottom: 0; width: 410px; height: 150px;
    background: linear-gradient(180deg, var(--brand-blue) 0%, var(--brand-blue-deep) 100%);
    padding: 26px 0 0 42px;
    clip-path: polygon(0 0, 60% 0, 64% 14px, 100% 14px, 100% 100%, 0 100%);
  }
  .person-name { color: var(--text-light); font-size: 22px; font-weight: 400; margin-top: 8px; }
  .person-role { color: var(--text-light); font-size: 13px; margin-top: 2px; }
  .person-address { color: var(--text-light); font-size: 13px; margin-top: 10px; line-height: 1.45; }

  .card--back .brand-logo-area { position: absolute; left: 42px; top: 74px; }
  .card--back .brand-name__text { font-size: 38px; letter-spacing: 1px; }
  .card--back .brand-name__tagline { font-size: 18px; letter-spacing: 1px; }
</style>
</head>
<body>
<main class="sheet">

  <section class="card card--front" aria-label="Business card front">
    <div class="brand-name">
      <span class="brand-name__square"></span>
      <span class="brand-name__text">
        <span>BEL Soravin</span>
        <span class="brand-name__tagline">Group of Companies</span>
      </span>
    </div>
    <p class="front-web">www.belsoravingroup.com</p>
  </section>

  <section class="card card--back" aria-label="Business card back">
    <div class="brand-logo-area">
      <div class="brand-name">
        <span class="brand-name__square"></span>
        <span class="brand-name__text">
          <span>BEL Soravin</span>
          <span class="brand-name__tagline">Group of Companies</span>
        </span>
      </div>
    </div>

    <aside class="contact-panel">
      <ul class="contact-list">
        <li>
          <svg viewBox="0 0 16 16"><path d="M3 1h3l1.5 4-2 1.2a9 9 0 0 0 4.3 4.3L11 8.5l4 1.5v3a2 2 0 0 1-2 2A12 12 0 0 1 1 3a2 2 0 0 1 2-2z"/></svg>
          0000 555 3131
        </li>
        <li>
          <svg viewBox="0 0 16 16"><path d="M4 0h8a1 1 0 0 1 1 1v14a1 1 0 0 1-1 1H4a1 1 0 0 1-1-1V1a1 1 0 0 1 1-1zm1 2v10h6V2zm3 11a1 1 0 1 0 0 2 1 1 0 0 0 0-2z"/></svg>
          0000 555 3131
        </li>
        <li>
          <svg viewBox="0 0 16 16"><path d="M4 0h7v4H4zM1 5h14v8h-3v3H4v-3H1zm4 6v4h6v-4z"/></svg>
          0000 555 3131
        </li>
        <li>
          <svg viewBox="0 0 16 16"><path d="M0 3h16v10H0zm1.5 1.2V12h13V4.2L8 9z"/></svg>
          korvan@belsoravingroup.com
        </li>
        <li>
          <svg viewBox="0 0 16 16"><path d="M8 0a8 8 0 1 0 0 16A8 8 0 0 0 8 0zm0 1.5c.9 0 2 2 2.3 5.5H5.7C6 3.5 7.1 1.5 8 1.5zM1.6 7h2.6c.1-2 .5-3.8 1.1-4.9A6.5 6.5 0 0 0 1.6 7zm0 2a6.5 6.5 0 0 0 3.7 4.9C4.7 12.8 4.3 11 4.2 9zm4.1 0h4.6C10 12.5 8.9 14.5 8 14.5S6 12.5 5.7 9zm6.1 0c-.1 2-.5 3.8-1.1 4.9A6.5 6.5 0 0 0 14.4 9zm2.6-2A6.5 6.5 0 0 0 10.7 2.1c.6 1.1 1 2.9 1.1 4.9z"/></svg>
          www.belsoravingroup.com
        </li>
      </ul>
    </aside>

    <div class="identity-band">
      <h1 class="person-name">Korvan EL Mistrani</h1>
      <p class="person-role">Operation Manager</p>
      <p class="person-address">BEL Soravin Group Of Companies<br>0/14 Marlow St Fenhaven,<br>QLD 0000</p>
    </div>
  </section>

</main>
</body>
</html>
```